Powerpoint Design and Build

We need to create PowerPoint for program called Kindled Horizons. Kindled Horizons is an online system that helps association volunteers track their volunteer hours and the impact that are having with engineering outreach initiatives.

We have an established logo for the brand, which you will find under Files.

The following colors are used in the brand:

Blue/green: PMS 3262 C

Purple: PMS 525 C

Lime: PMS 381 C

Grey: PMS Cool Grey 11

Headline and body fonts should be restricted to a common sans serif such as arial or helvetica

For reference, The tagline "Every Hour Matters" is set in Gotham Book; match to this.

The identity needs to be locked up with the Alliance of Rural Planners logo in grey, which you'll find attached. See the file "Kindled_horizons_lock-up.psd" for reference, but please recreate as a vector element.

As an idea of Powerpoint created for a different Alliance of Rural Planners program, place see the Lantern Powerpoint. FOR Reference only

NOTE: please maximize the area for content and stick to a white background.

Final deliverables are:

Design for presentation title slide, section title slide and content slide, including styles for headlines, subheads, bullet points and straight copy. Also include slide numbers in footer.

To repeat, we expect separate art elements created in Illustrator, and a completed Powerpoint template with master slides.

Target Market(s)

Professional and Collegiate Women in Engineering

Industry/Entity Type

Engineering

Requirements
Must have
• Design for presentation title slide, section title slide and content slide, including styles for headlines, subheads, bullet points and straight copy. Also include slide numbers in footer.

```html
<!DOCTYPE html>
<html lang="en">
<head>
<meta charset="utf-8">
<title>Kindled Horizons – Presentation Template</title>
<link rel="stylesheet" href="https://fonts.googleapis.com/css2?family=Arimo:wght@400;700&family=Montserrat:wght@400&family=Arvo:wght@700&display=swap">
<style>
:root{
  --teal:#00b2a9;
  --purple:#512d6d;
  --lime:#c4d600;
  --grey:#53565a;
  --grey-light:#8a8c8f;
  --rule:#d9d9d9;
  --stage:#ececec;
  --white:#ffffff;
}
*{box-sizing:border-box;margin:0;padding:0}
html,body{width:1200px;height:672px;overflow:hidden}
body{background:var(--stage);position:relative;font-family:"Arimo",Arial,sans-serif;color:var(--grey)}

.slide{position:absolute;width:264px;height:197px;background:var(--white);overflow:hidden;box-shadow:0 1px 3px rgba(0,0,0,.18)}
.slide-footer{position:absolute;left:0;right:0;bottom:0;height:13px;background:var(--grey);border-top:2px solid var(--purple);
  display:flex;justify-content:space-between;align-items:center;padding:0 8px 0 40px;font-size:4.5px;color:var(--white);font-weight:700}
.footer-mark{position:absolute;left:5px;bottom:4px;width:22px;height:22px;border-radius:50%;background:var(--white);border:3px solid var(--teal)}

.lockup{display:flex;align-items:center;gap:6px}
.lockup-dot{width:20px;height:20px;border-radius:50%;background:var(--teal);flex:none}
.lockup-name{font-size:15px;font-weight:400;color:var(--purple);line-height:1;white-space:nowrap}
.lockup-tagline{font-family:"Montserrat",Arial,sans-serif;font-size:4.5px;color:var(--grey);margin-top:2px;white-space:nowrap}
.lockup-divider{width:1px;height:16px;background:var(--grey-light);flex:none}
.lockup-partner{display:flex;align-items:center;gap:3px;font-size:5px;color:var(--grey);line-height:1.15;width:48px}
.lockup-partner::before{content:"";width:9px;height:9px;border-radius:50%;background:var(--grey-light);flex:none}

.headline{position:absolute;left:20px;top:10px;font-size:11px;font-weight:700;color:var(--purple);padding-bottom:2px;border-bottom:1px solid var(--rule);white-space:nowrap}
.copy{font-size:4.4px;line-height:1.45;color:var(--grey)}
.bullets{list-style:none;font-size:5px;color:var(--grey)}
.bullets li{position:relative;padding-left:8px;margin-bottom:4.5px;white-space:nowrap}
.bullets li::before{content:"";position:absolute;left:0;top:1px;width:3px;height:3px;background:var(--teal)}

.photo{position:absolute;background:linear-gradient(135deg,#d9719a,#a35772 45%,#c9c1b6)}

/* title slide */
.title-slide .lockup{position:absolute;left:14px;top:22px}
.title-main{position:absolute;left:0;right:0;top:92px;text-align:center;font-size:15px;font-weight:700;color:var(--purple)}
.title-desc{position:absolute;left:0;right:0;top:112px;text-align:center;font-size:9px;color:var(--grey)}

/* section slide */
.section-slide{width:267px;height:213px}
.section-slide .lockup{position:absolute;left:12px;top:26px}
.section-title{position:absolute;left:0;right:0;top:88px;text-align:center;font-size:40px;font-weight:400;color:var(--grey)}

/* table */
.data-table{position:absolute;left:20px;top:40px;width:224px;border-collapse:collapse;font-size:4px;color:var(--grey)}
.data-table th{background:var(--teal);color:var(--white);font-size:7px;font-weight:700;padding:3px 0}
.data-table td{padding:1.8px 6px;border-bottom:1px solid var(--rule);text-align:left}

/* thank you */
.thanks{position:absolute;left:0;right:0;top:10px;text-align:center;font-family:"Arvo",Georgia,serif;font-size:17px;color:var(--purple)}
.thanks-sub{position:absolute;left:0;right:0;top:32px;text-align:center;font-size:8px;font-weight:700;color:var(--teal)}
.thanks-slide .lockup{position:absolute;left:14px;top:58px}
.presented{position:absolute;left:0;right:0;top:112px;text-align:center;font-size:11px;font-weight:700;color:var(--grey)}

.columns{position:absolute;left:20px;top:38px;display:flex;gap:14px}
.columns .col{width:105px;font-size:4.3px;line-height:1.6}
.sub{color:var(--grey);margin-top:5px}
.arrow-item{position:relative;padding-left:6px;white-space:nowrap}
.arrow-item::before{content:"›";position:absolute;left:0;color:var(--teal)}
</style>
</head>
<body>

<!-- Title slide -->
<section class="slide title-slide" style="left:320px;top:16px">
  <div class="lockup">
    <span class="lockup-dot"></span>
    <div><div class="lockup-name">Kindled Horizons</div><div class="lockup-tagline">Every Hour Matters</div></div>
    <span class="lockup-divider"></span>
    <div class="lockup-partner">Alliance of Rural Planners</div>
  </div>
  <h1 class="title-main">TITLE OF PRESENTATION</h1>
  <p class="title-desc">Description</p>
  <span class="footer-mark"></span>
  <footer class="slide-footer"><span>Private/Confidential</span><span>www.kindledhorizons.org</span></footer>
</section>

<!-- Content: copy + bullets -->
<section class="slide" style="left:620px;top:16px">
  <h2 class="headline">LOREM IPSUM &nbsp;LOREM</h2>
  <p class="copy" style="position:absolute;left:20px;top:32px;width:226px">Lorem ipsum dolor sit amet, consectetuer adipiscing elit, sed diam nonummy nibh euismod tincidunt ut laoreet dolore magna aliquam erat volutpat. Ut wisi enim ad minim veniam, quis nostrud exerci tation ullamcorper suscipit lobortis nisl ut aliquip ex ea commodo consequat. Duis autem vel eum iriure dolor in hendrerit in vulputate velit esse molestie.</p>
  <ul class="bullets" style="position:absolute;left:22px;top:76px">
    <li>Lorem ipsum &nbsp;Lorem ipsum &nbsp;Lorem</li>
    <li>Lorem ipsum Lorem Lorem</li>
    <li>Lorem ipsum Lorem Lorem ipsum &nbsp;Lorem ipsum</li>
    <li>Lorem ipsum orem Lorem ipsum &nbsp;Lo</li>
    <li>Lorem ipsum Lorem</li>
  </ul>
  <span class="footer-mark"></span>
  <footer class="slide-footer"><span>Private/Confidential</span><span>www.kindledhorizons.org</span></footer>
</section>

<!-- Content: copy + photo -->
<section class="slide" style="left:920px;top:16px">
  <h2 class="headline">LOREM IPSUM &nbsp;LOREM</h2>
  <p class="copy" style="position:absolute;left:20px;top:32px;width:226px">Lorem ipsum dolor sit amet, consectetuer adipiscing elit, sed diam nonummy nibh euismod tincidunt ut laoreet dolore magna aliquam erat volutpat. Ut wisi enim ad minim veniam, quis nostrud exerci tation ullamcorper suscipit lobortis nisl ut aliquip ex ea commodo.</p>
  <div class="photo" role="img" aria-label="Photo of volunteers working together at an outreach event" style="left:66px;top:62px;width:130px;height:80px"></div>
  <span class="footer-mark"></span>
  <footer class="slide-footer"><span>Private/Confidential</span><span>www.kindledhorizons.org</span></footer>
</section>

<!-- Section slide -->
<section class="slide section-slide" style="left:16px;top:227px">
  <div class="lockup">
    <span class="lockup-dot"></span>
    <div><div class="lockup-name">Kindled Horizons</div><div class="lockup-tagline">Every Hour Matters</div></div>
    <span class="lockup-divider"></span>
    <div class="lockup-partner">Alliance of Rural Planners</div>
  </div>
  <h1 class="section-title">Part 3</h1>
  <span class="footer-mark"></span>
  <footer class="slide-footer"><span>Private/Confidential</span><span>www.kindledhorizons.org</span></footer>
</section>

<!-- Content: text + photo with lockup -->
<section class="slide" style="left:320px;top:229px">
  <div class="lockup" style="position:absolute;left:12px;top:10px;transform:scale(.8);transform-origin:left top">
    <span class="lockup-dot"></span>
    <div><div class="lockup-name">Kindled Horizons</div><div class="lockup-tagline">Every Hour Matters</div></div>
    <span class="lockup-divider"></span>
    <div class="lockup-partner">Alliance of Rural Planners</div>
  </div>
  <h2 class="headline" style="top:46px">LOREM IPSUM</h2>
  <p class="copy" style="position:absolute;left:12px;top:68px;width:110px">Lorem ipsum dolor sit amet, consectetuer adipiscing elit, sed diam nonummy nibh euismod tincidunt ut laoreet dolore magna aliquam erat volutpat. Ut wisi enim ad minim veniam, quis nostrud exerci tation ullamcorper suscipit lobortis nisl ut aliquip ex ea commodo consequat.</p>
  <div class="photo" role="img" aria-label="Photo of volunteers gathered around a table" style="left:134px;top:60px;width:130px;height:98px"></div>
  <span class="footer-mark"></span>
  <footer class="slide-footer"><span>Private/Confidential</span><span>www.kindledhorizons.org</span></footer>
</section>

<!-- Content: table -->
<section class="slide" style="left:620px;top:229px">
  <h2 class="headline">LOREM IPSUM</h2>
  <table class="data-table">
    <thead><tr><th colspan="4">Lorem ipsum Lorem ipsum Lorem ipsum</th></tr></thead>
    <tbody>
      <tr><td>Lorem ipsum</td><td>Lorem ipsum</td><td>Lorem ipsum</td><td>Lorem ipsum</td></tr>
      <tr><td>Lorem ipsum</td><td>Lorem ipsum</td><td>Lorem ipsum</td><td>Lorem ipsum</td></tr>
      <tr><td>Lorem ipsum</td><td>Lorem ipsum</td><td>Lorem ipsum</td><td>Lorem ipsum</td></tr>
      <tr><td>Lorem ipsum</td><td>Lorem ipsum</td><td>Lorem ipsum</td><td>Lorem ipsum</td></tr>
      <tr><td>Lorem ipsum</td><td>Lorem ipsum</td><td>Lorem ipsum</td><td>Lorem ipsum</td></tr>
      <tr><td>Lorem ipsum</td><td>Lorem ipsum</td><td>Lorem ipsum</td><td>Lorem ipsum</td></tr>
      <tr><td>Lorem ipsum</td><td>Lorem ipsum</td><td>Lorem ipsum</td><td>Lorem ipsum</td></tr>
      <tr><td>Lorem ipsum</td><td>Lorem ipsum</td><td>Lorem ipsum</td><td>Lorem ipsum</td></tr>
      <tr><td>Lorem ipsum</td><td>Lorem ipsum</td><td>Lorem ipsum</td><td>Lorem ipsum</td></tr>
    </tbody>
  </table>
  <span class="footer-mark"></span>
  <footer class="slide-footer"><span>Private/Confidential</span><span>www.kindledhorizons.org</span></footer>
</section>

<!-- Content: diagram -->
<section class="slide" style="left:920px;top:229px">
  <h2 class="headline">LOREM IPSUM</h2>
  <svg width="264" height="197" viewBox="0 0 264 197" style="position:absolute;left:0;top:0" font-family="Arimo, Arial, sans-serif" font-size="3.6">
    <g stroke="#7fcfc9" stroke-width=".8" fill="none">
      <path d="M32 44h200M32 44v18M89 44v18M146 44v18M203 44v18"/>
      <path d="M46 48v105M103 48v105M160 48v105M217 48v105"/>
      <path d="M60 78h29M117 78h29M174 78h29M60 108h29M117 108h29M174 108h29"/>
    </g>
    <g fill="#00b2a9">
      <rect x="28" y="37" width="36" height="11" rx="1.5"/><rect x="85" y="37" width="36" height="11" rx="1.5"/>
      <rect x="142" y="37" width="36" height="11" rx="1.5"/><rect x="199" y="37" width="36" height="11" rx="1.5"/>
    </g>
    <g fill="#fff" text-anchor="middle" font-weight="700">
      <text x="46" y="43.5">Lorem ipsum</text><text x="103" y="43.5">Lorem ipsum</text>
      <text x="160" y="43.5">Lorem ipsum</text><text x="217" y="43.5">Lorem ipsum</text>
    </g>
    <defs>
      <g id="cylinder">
        <path d="M-14 -7v14a14 3.5 0 0 0 28 0v-14z" fill="#00b2a9"/>
        <ellipse cx="0" cy="-7" rx="14" ry="3.5" fill="#5cc9c2"/>
        <text x="0" y="3" fill="#fff" text-anchor="middle" font-weight="700">Lorem</text>
      </g>
    </defs>
    <use href="#cylinder" x="46" y="76"/><use href="#cylinder" x="103" y="76"/><use href="#cylinder" x="160" y="76"/><use href="#cylinder" x="217" y="76"/>
    <use href="#cylinder" x="46" y="106"/><use href="#cylinder" x="103" y="106"/><use href="#cylinder" x="160" y="106"/><use href="#cylinder" x="217" y="106"/>
    <use href="#cylinder" x="46" y="138"/><use href="#cylinder" x="103" y="138"/><use href="#cylinder" x="160" y="138"/><use href="#cylinder" x="217" y="138"/>
  </svg>
  <span class="footer-mark"></span>
  <footer class="slide-footer"><span>Private/Confidential</span><span>www.kindledhorizons.org</span></footer>
</section>

<!-- Content: bullet list -->
<section class="slide" style="left:320px;top:456px">
  <h2 class="headline">LOREM IPSUM</h2>
  <ul class="bullets" style="position:absolute;left:22px;top:36px;font-size:4.6px">
    <li>Lorem ipsum dolor sit amet, consectetuer adipiscing elit, sed diam non</li>
    <li>Lorem ipsum dolor sit amet, consectetuer adipiscing elit, sed diam non</li>
    <li>Lorem ipsum dolor sit amet, consectetuer adipiscing elit, sed diam non</li>
    <li>Lorem ipsum dolor sit amet, consectetuer adipiscing elit, sed diam non</li>
    <li>Lorem ipsum dolor sit amet, consectetuer adipiscing elit, sed diam non</li>
    <li>Lorem ipsum dolor sit amet, consectetuer adipiscing elit, sed diam non</li>
    <li>Lorem ipsum dolor sit amet, consectetuer</li>
  </ul>
  <span class="footer-mark"></span>
  <footer class="slide-footer"><span>Private/Confidential</span><span>www.kindledhorizons.org</span></footer>
</section>

<!-- Content: subheads in columns -->
<section class="slide" style="left:620px;top:456px">
  <h2 class="headline">LOREM IPSUM</h2>
  <div class="columns">
    <div class="col">
      <div class="sub">Sub Title 1</div>
      <div class="arrow-item">Lorem ipsum dolor sit amet, wisi</div>
      <div class="arrow-item">Adipiscing elit, sed diam non euismod</div>
      <div class="sub">Sub Title 2</div>
      <div class="arrow-item">Lorem ipsum dolor sit amet, wisi</div>
      <div class="arrow-item">Adipiscing elit, sed diam non euismod</div>
      <div class="sub">Sub Title 3</div>
      <div class="arrow-item">Lorem ipsum dolor sit amet, wisi</div>
      <div class="arrow-item">Adipiscing elit, sed diam non euismod</div>
    </div>
    <div class="col">
      <div class="sub">Sub Title 1</div>
      <div class="arrow-item">Lorem ipsum dolor sit amet, consectetuer</div>
      <div class="sub">Sub Title 2</div>
      <div class="arrow-item">Lorem ipsum dolor sit amet, consectetuer</div>
      <div class="arrow-item">Adipiscing elit, sed diam nibh euismod</div>
      <div class="sub">Sub Title 3</div>
      <div class="arrow-item">Lorem ipsum dolor sit amet, consectetuer</div>
      <div class="arrow-item">Adipiscing elit, sed diam nibh euismod</div>
    </div>
  </div>
  <span class="footer-mark"></span>
  <footer class="slide-footer"><span>Private/Confidential</span><span>www.kindledhorizons.org</span></footer>
</section>

<!-- Closing slide -->
<section class="slide thanks-slide" style="left:920px;top:456px">
  <h1 class="thanks">Thank You!</h1>
  <p class="thanks-sub">For your attention</p>
  <div class="lockup">
    <span class="lockup-dot"></span>
    <div><div class="lockup-name">Kindled Horizons</div><div class="lockup-tagline">Every Hour Matters</div></div>
    <span class="lockup-divider"></span>
    <div class="lockup-partner">Alliance of Rural Planners</div>
  </div>
  <p class="presented">Presented By</p>
  <span class="footer-mark"></span>
  <footer class="slide-footer"><span>Private/Confidential</span><span>www.kindledhorizons.org</span></footer>
</section>

</body>
</html>
```